Restaurant needs a vertical banner for fried catfish

Our restaurant is looking for an eye-catching 78.75in. x 36in. vertical physical banner ad for our fried catfish. Photos for the fried catfish will be provided as a reference but we will also accept anything similar to the photo. We will be using the following as our receptacle: https://www.plankoria.example/banner-stand/retractable-banner-stands/
The design must incorporate the following flavor texts:
Fried Catfish
Always Fresh!
Made from Scratch
Hand-cut Fillets
The Best Catfish in Texas
Served with fries, hush puppies, and a 32oz fountain drink
Also available by the pound!
The final design should be creative, professional, and eye-catching for customers.
Updates
Colors
Designer to choose colors to be used in the design.
Requirements
Must have
- We are open to any and all design elements, albeit the 'flavor texts' should not overpower, but complement the fried catfish photo. 'Fried Catfish' can be used in lieu of a main title/logo.
Nice to have
- Transparent or textured backgrounds that can encompass any or all part of the banner such as a cutting board, shadows, abstract, etc to show depth are a plus.
- Use of vectors or objects such as ribbons or shapes to encapsulate the 'flavor texts' are also encouraged.

```html
<!DOCTYPE html>
<html lang="en">
<head>
<meta charset="utf-8">
<title>Fried Catfish Banner</title>
<link href="https://fonts.googleapis.com/css2?family=Alfa+Slab+One&family=Bebas+Neue&display=swap" rel="stylesheet">
<style>
  :root {
    --page-bg: #e4e4e4;
    --banner-white: #f7f7f5;
    --title-ink: #2a2a2a;
    --brand-red: #9b0000;
    --accent-yellow: #f5b800;
    --text-white: #ffffff;
    --text-dark: #1c1c1c;
    --food-gold: #c9862b;
    --food-light: #e9b35a;
    --veg-red: #d8351e;
    --veg-yellow: #e8d23a;
  }
  html, body {
    margin: 0;
    width: 1200px;
    height: 1200px;
    overflow: hidden;
    background: radial-gradient(circle at 50% 40%, #f2f2f2, var(--page-bg));
  }
  .banner {
    position: absolute;
    left: 343px;
    top: 40px;
    width: 513px;
    height: 1120px;
    background: var(--banner-white);
    box-shadow: 0 14px 30px rgba(0,0,0,0.18);
    overflow: hidden;
    font-family: "Bebas Neue", "Arial Narrow", sans-serif;
  }
  .banner-art {
    position: absolute;
    inset: 0;
  }
  .title {
    position: absolute;
    left: 0;
    width: 100%;
    text-align: center;
    margin: 0;
    font-family: "Alfa Slab One", Georgia, serif;
    font-weight: 400;
    color: var(--title-ink);
    line-height: 1;
  }
  .title-top { top: 58px; font-size: 98px; letter-spacing: 3px; }
  .title-bottom { top: 152px; font-size: 72px; letter-spacing: 1px; }
  .tagline {
    position: absolute;
    left: 66px;
    top: 293px;
    width: 381px;
    height: 51px;
    background: var(--brand-red);
    color: var(--text-white);
    font-size: 35px;
    line-height: 53px;
    text-align: center;
    letter-spacing: 1px;
  }
  .features {
    position: absolute;
    left: 0;
    top: 770px;
    width: 100%;
    margin: 0;
    padding: 0;
    list-style: none;
    text-align: center;
  }
  .features li {
    color: var(--text-white);
    font-size: 44px;
    line-height: 53px;
    letter-spacing: 1px;
  }
  .features .chevron {
    color: var(--accent-yellow);
    margin-right: 8px;
  }
  .serving {
    position: absolute;
    left: 45px;
    top: 940px;
    width: 423px;
    height: 87px;
    background: var(--text-white);
    color: var(--text-dark);
    font-size: 25px;
    line-height: 28px;
    text-align: center;
    display: flex;
    align-items: center;
    justify-content: center;
    letter-spacing: 0.5px;
  }
  .by-pound {
    position: absolute;
    left: 0;
    top: 1043px;
    width: 100%;
    text-align: center;
    color: var(--accent-yellow);
    font-size: 26px;
    letter-spacing: 1px;
  }
</style>
</head>
<body>
  <div class="banner">
    <svg class="banner-art" width="513" height="1120" viewBox="0 0 513 1120" xmlns="http://www.w3.org/2000/svg">
      <defs>
        <linearGradient id="platterTone" x1="0" y1="0" x2="0" y2="1">
          <stop offset="0" stop-color="var(--veg-red)"/>
          <stop offset="0.18" stop-color="var(--veg-yellow)"/>
          <stop offset="0.35" stop-color="#f1ede4"/>
          <stop offset="0.5" stop-color="var(--food-gold)"/>
          <stop offset="0.8" stop-color="var(--food-light)"/>
          <stop offset="1" stop-color="#f3e6c8"/>
        </linearGradient>
        <radialGradient id="insetTone" cx="0.45" cy="0.5" r="0.6">
          <stop offset="0" stop-color="var(--food-gold)"/>
          <stop offset="0.7" stop-color="var(--food-light)"/>
          <stop offset="1" stop-color="#f1ede4"/>
        </radialGradient>
      </defs>
      <rect class="platter-photo" role="img" aria-label="Plate of golden fried catfish fillets with fries and tartar sauce, tomatoes and lemons behind" x="0" y="220" width="513" height="520" fill="url(#platterTone)"/>
      <path class="top-panel" d="M0 0 H513 V229 Q 330 380 0 303 Z" fill="var(--banner-white)"/>
      <path class="bottom-panel" d="M0 541 C 110 690 300 745 513 720 V1120 H0 Z" fill="var(--brand-red)"/>
      <circle class="inset-ring" cx="137" cy="653" r="103" fill="var(--accent-yellow)"/>
      <circle class="inset-photo" role="img" aria-label="Close-up of fried catfish fillets with hush puppies and dipping sauce" cx="139" cy="653" r="96" fill="url(#insetTone)"/>
    </svg>

    <h1 class="title title-top">FRIED</h1>
    <p class="title title-bottom">CATFISH</p>
    <div class="tagline">The Best Catfish in Texas</div>

    <ul class="features">
      <li><span class="chevron">»</span>Always Fresh</li>
      <li><span class="chevron">»</span>Made from Scratch</li>
      <li><span class="chevron">»</span>Handcut Fillets</li>
    </ul>

    <div class="serving">Served with fries hush puppies and<br>a 32oz fountain drink</div>
    <div class="by-pound">Also available by the pound</div>
  </div>
</body>
</html>
```